Tolvik service sheets and folder

A set of 12 Service sheets plus a rate card to be inserted into a folder - each to be designed and formatted.
A4
Portrait
- the idea is to keep things simple and crisp.
I would use the logo (see attached .ai file) at the top and maybe an separate image to go with each sheet

Around 350 words per page (see attached example)
The format is mainly text and bullet points, but each page will be same layout (just a different image as indicated above).

Need to factor in a folder to hold the service sheets.

The documents to have a good sales impact and your experience and advice on best ideas would be welcome. The key is to keep it crisp, elegant & professional for financial services.

The output files should be in PDF and raw file formats so that printing can be managed easily in future., Details for my new Catalogue Design Project will be added soon.

Industry/Entity Type

Financial

Requirements
Must have
• Inspire us!
Should not have
• No images of people or parts (like hands, arms) etc

```html
<!DOCTYPE html>
<html lang="en">
<head>
<meta charset="utf-8">
<title>Tolvik Service Sheets</title>
<link rel="stylesheet" href="https://fonts.googleapis.com/css2?family=Roboto+Condensed:wght@300;400;700&family=Montserrat:wght@300;600&display=swap">
<style>
:root{
  --backdrop:#a8a8a8;
  --paper:#ffffff;
  --panel:#ececec;
  --ink:#4a4a4a;
  --ink-soft:#5c5c5c;
  --brand:#3a3a3a;
  --brand-dot:#8a8a8a;
  --cover-text:#ffffff;
}
*{box-sizing:border-box;margin:0;padding:0}
html,body{width:1200px;height:920px;overflow:hidden}
body{background:var(--backdrop);position:relative;font-family:"Roboto Condensed",Arial,sans-serif;color:var(--ink)}
.sheet{position:absolute;width:269px;height:382px;background:var(--paper);box-shadow:0 1px 4px rgba(0,0,0,.25);overflow:hidden}
.row-top{top:45px}
.row-bottom{top:473px}
.col-1{left:37px}.col-2{left:321px}.col-3{left:606px}.col-4{left:893px}
.panel{position:absolute;left:10px;right:10px;top:12px;bottom:12px;background:var(--panel)}
.photo{position:absolute;left:0;right:0;top:132px;height:201px}
.brand{position:absolute;left:0;right:0;bottom:22px;display:flex;justify-content:center;align-items:center;gap:4px;font-size:8px;font-weight:700;letter-spacing:.3px;color:var(--brand)}
.brand-dot{width:9px;height:9px;border-radius:50%;background:var(--brand-dot)}
.lead{position:absolute;left:28px;right:26px;top:40px;font-weight:300;font-size:14px;line-height:18px;color:var(--ink)}
.lead.near{left:27px;top:30px}
.body-copy{position:absolute;left:21px;right:20px;top:25px;font-weight:300;font-size:8.2px;line-height:10.6px;color:var(--ink)}
.columns{position:absolute;left:24px;right:18px;top:27px;display:flex;gap:10px}
.columns section{flex:1}
.columns h2{font-size:7.5px;font-weight:700;letter-spacing:.2px;margin-bottom:3px;color:var(--ink)}
.columns ul{list-style:none}
.columns li{position:relative;padding-left:7px;font-size:6.2px;line-height:8px;font-weight:300;margin-bottom:1px}
.columns li::before{content:"";position:absolute;left:0;top:2.5px;width:3px;height:3px;background:var(--ink-soft)}
.contact{position:absolute;left:30px;right:18px;top:30px;font-weight:300;font-size:10px;line-height:13px}
.disclaimer{position:absolute;left:30px;right:20px;top:72px;font-size:4px;line-height:4.9px;color:var(--ink-soft)}
.disclaimer strong{display:block;font-size:4.6px}
.cover .cover-photo{position:absolute;left:9px;right:9px;top:10px;bottom:12px;background:linear-gradient(#4d8fcc 0%,#8fbfdc 28%,#5f97a8 52%,#3f7c86 66%,#2f5f6a 78%,#6a6762 84%,#4b4642 100%)}
.cover-title{position:absolute;left:27px;top:186px;font-family:"Montserrat",Arial,sans-serif;font-weight:300;font-size:21px;line-height:27px;color:var(--cover-text)}
.cover-sub{position:absolute;left:27px;top:268px;font-family:"Montserrat",Arial,sans-serif;font-weight:600;font-size:10px;color:var(--cover-text)}
.cover .brand{left:auto;right:16px;top:26px;bottom:auto;color:var(--cover-text)}
.cover .brand-dot{background:var(--cover-text)}
</style>
</head>
<body>

<div class="sheet cover row-top col-1">
  <div class="cover-photo" role="img" aria-label="City skyline over a calm bay with a life ring on a wooden jetty"></div>
  <div class="brand"><span class="brand-dot"></span>TOLVIK</div>
  <h1 class="cover-title">Investment<br>Management<br>Services</h1>
  <p class="cover-sub">Discretionary</p>
</div>

<div class="sheet row-top col-2">
  <div class="panel"></div>
  <p class="lead">Simplifying investing;<br>with your portfolio<br>managed by professionals</p>
  <div class="photo" role="img" aria-label="Aerial view of dense city towers" style="background:linear-gradient(#c9c4bd 0%,#8b8279 30%,#5c534b 60%,#3b352f 100%)"></div>
  <div class="brand"><span class="brand-dot"></span>TOLVIK</div>
</div>

<div class="sheet row-top col-3">
  <div class="panel"></div>
  <p class="lead near">A bespoke service tailored to your needs, with a dedicated investment manager taking over the burden of monitoring and managing your portfolio of investments.</p>
  <div class="photo" role="img" aria-label="Glass skyscrapers seen from below against a pale sky" style="background:radial-gradient(circle at 50% 40%,#e8f2fb 0%,#a9c8e4 35%,#4f7fae 70%,#23476f 100%)"></div>
  <div class="brand"><span class="brand-dot"></span>TOLVIK</div>
</div>

<div class="sheet row-top col-4">
  <div class="panel"></div>
  <p class="body-copy">Our role is to assist investors acquire a stake in the world economy through diversified portfolios. Investment processes blend our strategic view, a tactical overlay, an asset allocation policy and research of individual investment opportunities on a long term basis. We do not confine ourselves to a particular methodology, but we look for value, using such traditional measures as yield, price to book and the discounted value of cash flows. We aim to invest in companies that grow their dividends in the belief that an increasing income supports capital values.</p>
  <div class="photo" role="img" aria-label="Night city towers with colourful light trails" style="background:linear-gradient(135deg,#0b1633 0%,#1c3a7a 35%,#b5447a 60%,#f2b23a 80%,#2a1a3a 100%)"></div>
  <div class="brand"><span class="brand-dot"></span>TOLVIK</div>
</div>

<div class="sheet row-bottom col-1">
  <div class="panel"></div>
  <p class="body-copy" style="top:32px">The Discretionary Investment Management Service passes the burden of managing your portfolio of investments to a dedicated investment manager. Investments are targeted to provide the best returns matched to your stated risk profile and investment objectives. Your investment manager is available to discuss any aspect of your investments and you will be regularly updated with the performance of your portfolio.</p>
  <div class="photo" role="img" aria-label="Black and white view of city skyscrapers" style="background:linear-gradient(#e6e8ea 0%,#9ea3a8 35%,#5d6267 70%,#2e3236 100%)"></div>
  <div class="brand"><span class="brand-dot"></span>TOLVIK</div>
</div>

<div class="sheet row-bottom col-2">
  <div class="panel"></div>
  <div class="columns">
    <section>
      <h2>KEY FEATURES</h2>
      <ul>
        <li>A fully tailored investment management service with access to a personal investment manager.</li>
        <li>Each portfolio fully tailored to fulfill your individual requirements and monitored to ensure lifestyle changes are duly considered.</li>
        <li>A flexible product including access to investment expertise in smaller companies and derivatives if desired.</li>
        <li>Independent and unbiased advice.</li>
      </ul>
    </section>
    <section>
      <h2>RISK</h2>
      <ul>
        <li>The value of your investments and any income from them may go down and you may get back less than you invested.</li>
        <li>If you are unsure about the suitability of the products please contact us for advice.</li>
      </ul>
    </section>
  </div>
  <div class="photo" role="img" aria-label="Suspension bridge and city skyline across a river at dusk" style="background:linear-gradient(#3c4e6b 0%,#c9a66b 35%,#4d5f72 55%,#1e3a4a 80%,#0f2230 100%)"></div>
  <div class="brand"><span class="brand-dot"></span>TOLVIK</div>
</div>

<div class="sheet row-bottom col-3">
  <div class="panel"></div>
  <div class="columns">
    <section>
      <h2>ADDITIONAL FEATURES</h2>
      <ul>
        <li>Minimum portfolio size of GBP100,000.</li>
        <li>On-line access to review holdings.</li>
        <li>Regular portfolio valuations provided.</li>
        <li>Nominee service for custody of assets globally.</li>
        <li>Investment income transferred to an interest bearing account.</li>
        <li>Derivatives can be used as part of a hedging or covered income enhancement strategy, where required.</li>
      </ul>
    </section>
    <section>
      <h2>ASSOCIATED SERVICES</h2>
      <ul>
        <li>ISAs: Managed and Self Select.</li>
        <li>Managed Funds Service</li>
        <li>Independent SIPP Investment Management</li>
        <li>Advisory Dealing</li>
      </ul>
    </section>
  </div>
  <div class="photo" role="img" aria-label="Historic bascule bridge over a river with a flag and a passing boat" style="background:linear-gradient(#2f66b8 0%,#8fb3de 40%,#b9b3a6 62%,#3f4a55 82%,#20303c 100%)"></div>
  <div class="brand"><span class="brand-dot"></span>TOLVIK</div>
</div>

<div class="sheet row-bottom col-4">
  <div class="panel"></div>
  <p class="contact">For a confidential discussion please contact us on:<br>+44 (0)20 7946 0123 or via our website http://www.tolvik.com.</p>
  <p class="disclaimer"><strong>Disclaimer:</strong>Tolvik operates as a division of a regulated trading firm under a formal services agreement and is authorised by the relevant financial authority. This communication is for information only and does not constitute advice or an offer to buy or sell any investment. Past performance is not a guide to future returns, and the value of investments may fall as well as rise. Please read all product documents before investing and contact your investment manager if you have any questions about suitability.</p>
  <div class="photo" role="img" aria-label="Aerial view of a city at golden hour" style="background:linear-gradient(#9fb4c8 0%,#d8a56a 35%,#b07a45 60%,#5e4330 100%)"></div>
  <div class="brand"><span class="brand-dot"></span>TOLVIK</div>
</div>

</body>
</html>
```